Business Card Design Project

Im an electrician and my company name is Brightway Electrical
My main work is installing Lighting and Power Points, Home Theater Systems, TVS, Phones and Data
Im looking a business card, something nice, clean, modern and not to cluttered
Im open to sugestions
I dont mind if the "Services" is on the back on the business card
colours black, grey, white or the blue colour of my logo are prefered but not compulsory
any questions just message me
and please make it so if i need to edit the writing can do it easy. maybe by making it a seperate layer ?
My Details are.
Name - Peter Hollis
Job Title - Licenced Electrician
Mobile - 027 530 2174
Email - peter@brightwayelectrical.co.nz
Web - www.brightwayelectrical.co.nz
Services
Residential / Commercial
Lighting & Power
Heating & Ventilation
Automation
Phone & Data
Home Cinema
Sound Systems
TV, Antenna & Satellite
Digital Upgrades

```html
<!DOCTYPE html>
<html lang="en">
<head>
<meta charset="utf-8">
<title>Brightway Electrical – Business Card</title>
<link rel="stylesheet" href="https://fonts.googleapis.com/css2?family=Source+Sans+3:wght@400;600;700&display=swap">
<style>
  :root {
    --page-bg: #e9e9e7;
    --card-dark: #0d1b20;
    --card-mid: #16282e;
    --accent: #20b4d4;
    --card-shadow: rgba(0, 0, 0, 0.35);
  }
  * { margin: 0; padding: 0; box-sizing: border-box; }
  html, body {
    width: 1200px; height: 1000px; overflow: hidden;
    background: var(--page-bg);
    font-family: "Source Sans 3", "Myriad Pro", Arial, sans-serif;
  }
  .card-set {
    position: absolute; top: 350px; left: 47px;
    display: flex; gap: 37px;
  }
  .card {
    position: relative; width: 535px; height: 300px;
    color: var(--accent);
    box-shadow: 0 6px 14px var(--card-shadow);
    overflow: hidden;
  }
  .card-texture {
    position: absolute; inset: 0;
    background: linear-gradient(135deg, var(--card-mid) 0%, var(--card-dark) 60%, #0b171b 100%);
  }
  .brand {
    position: absolute; display: flex; align-items: center; gap: 8px;
    font-weight: 700; color: var(--accent); text-transform: uppercase;
  }
  .brand-mark { width: 14px; height: 14px; background: var(--accent); }
  .front .brand { top: 58px; left: 45px; font-size: 18px; letter-spacing: 0.5px; }
  .identity {
    position: absolute; top: 50px; left: 290px; width: 200px; text-align: center;
  }
  .identity .name { font-size: 23px; font-weight: 600; line-height: 1.2; }
  .identity .role { font-size: 19px; font-weight: 400; line-height: 1.2; }
  .contacts {
    position: absolute; top: 168px; left: 274px; list-style: none;
  }
  .contacts li {
    display: flex; align-items: center; gap: 8px;
    font-size: 16px; height: 28.5px;
  }
  .contacts svg { width: 20px; height: 20px; flex: none; }
  .back .brand {
    top: 50%; left: 40px; transform: translateY(-50%);
    flex-direction: column; align-items: flex-start; gap: 4px;
    font-size: 30px; line-height: 1.05;
  }
  .services { position: absolute; top: 22px; left: 294px; }
  .services h2 { font-size: 17px; font-weight: 700; margin-bottom: 6px; }
  .services ul { list-style: none; }
  .services li { font-size: 17px; line-height: 28.5px; }
  .services li::before { content: "• "; }
</style>
</head>
<body>
<main class="card-set">
  <section class="card front">
    <div class="card-texture" role="img" aria-label="Dark card background with faint repeating brand pattern"></div>
    <div class="brand"><span class="brand-mark"></span>Brightway Electrical</div>
    <div class="identity">
      <p class="name">Peter Hollis</p>
      <p class="role">Licenced Electrician</p>
    </div>
    <ul class="contacts">
      <li>
        <svg viewBox="0 0 20 20" fill="none" stroke="currentColor" stroke-width="1.3"><circle cx="10" cy="10" r="9"/><rect x="7" y="4.5" width="6" height="11" rx="1"/><line x1="9" y1="13.5" x2="11" y2="13.5"/></svg>
        027 530 2174
      </li>
      <li>
        <svg viewBox="0 0 20 20" fill="none" stroke="currentColor" stroke-width="1.3"><circle cx="10" cy="10" r="9"/><rect x="5" y="6.5" width="10" height="7"/><polyline points="5,6.5 10,10.5 15,6.5"/></svg>
        peter@brightwayelectrical.co.nz
      </li>
      <li>
        <svg viewBox="0 0 20 20" fill="none" stroke="currentColor" stroke-width="1.3"><circle cx="10" cy="10" r="9"/><ellipse cx="10" cy="10" rx="4" ry="9"/><line x1="1" y1="10" x2="19" y2="10"/><line x1="2.5" y1="5.5" x2="17.5" y2="5.5"/><line x1="2.5" y1="14.5" x2="17.5" y2="14.5"/></svg>
        www.brightwayelectrical.co.nz
      </li>
    </ul>
  </section>

  <section class="card back">
    <div class="card-texture" role="img" aria-label="Dark card background with faint repeating brand pattern"></div>
    <div class="brand"><span>Brightway</span><span>Electrical</span></div>
    <div class="services">
      <h2>Residential / Commercial</h2>
      <ul>
        <li>Lighting &amp; Power</li>
        <li>Heating &amp; Ventilation</li>
        <li>Automation</li>
        <li>Phone &amp; Data</li>
        <li>Home Cinema</li>
        <li>Sound Systems</li>
        <li>TV, Antenna &amp; Satellite</li>
        <li>Digital Upgrades</li>
      </ul>
    </div>
  </section>
</main>
</body>
</html>
```